Graduates Circle Sponsorship Brochure

The University of Glenmarrow Alumni Club of New York is putting together a brochure to solicit corporate sponsors for our 5th annual black tie gala in downtown Manhattan.
The Graduates Circle works to benefit both the alumni community and to give back to the University. Our Lantern Dance seeks to bring together former students, friends, and family of Glenmarrow to remind them of their own Lantern Dance experience during university. We are also promoting Scottish-American relations, and want to make clear to sponsors the benefit of access to our demographic.

Target Market(s)

Corporations, Special Interest Groups, parties with affiliation to Scotland and the UK.

Industry/Entity Type

Non-Profit

Font styles to use
Serif

Colors
ec1f27
0255a3

Requirements
Must have
• Clear details about the separation of sponsorship price points, emphasis on the potential impact and benefit of partnership.
Nice to have
• Some big pictures and lots of icons to show the different sponsorship levels.

```html
<!DOCTYPE html>
<html lang="en">
<head>
<meta charset="utf-8">
<title>Lantern Dance Sponsorship Brochure – Cover</title>
<link href="https://fonts.googleapis.com/css2?family=Cormorant+Garamond:wght@500;600;700&display=swap" rel="stylesheet">
<style>
  :root {
    --backdrop: #0b7fc0;
    --page-light: #eeeef0;
    --page-light-edge: #d6d7d9;
    --ink: #121212;
    --ink-soft: #1c1c1c;
    --gold: #d9ae4a;
    --gold-light: #f0d27a;
    --gold-deep: #a9781f;
    --cream: #f1e6c4;
  }
  * { margin: 0; padding: 0; box-sizing: border-box; }
  html, body { width: 1200px; height: 1000px; overflow: hidden; }
  body {
    background: var(--backdrop);
    font-family: "Cormorant Garamond", Georgia, serif;
    position: relative;
  }
  .spread {
    position: absolute; left: 139px; top: 174px;
    width: 919px; height: 651px;
    display: flex;
    box-shadow: 0 8px 18px rgba(0,0,0,.3);
  }
  .back-page {
    width: 461px; height: 651px; position: relative;
    background: radial-gradient(ellipse at 50% 40%, #fbfbfc 0%, var(--page-light) 45%, var(--page-light-edge) 100%);
  }
  .address-plate {
    position: absolute; left: 55px; top: 246px;
    width: 351px; height: 160px;
    background: var(--ink);
    box-shadow: 0 3px 8px rgba(0,0,0,.35);
    display: flex; align-items: center; justify-content: center;
  }
  .address-plate::before {
    content: ""; position: absolute; inset: 6px;
    border: 2px solid var(--gold);
  }
  .address-plate p {
    color: var(--gold); font-weight: 600; font-size: 27px;
    line-height: 1.35; text-align: center;
  }
  .front-page {
    width: 458px; height: 651px; position: relative;
    background: linear-gradient(180deg, #161616 0%, var(--ink) 60%, #0d0d0d 100%);
    overflow: hidden;
  }
  .front-art { position: absolute; inset: 0; }
  .front-page .event-title {
    position: absolute; left: 0; right: 0; top: 52px;
    text-align: center; color: var(--gold);
    font-weight: 600; font-size: 48px; line-height: 1.3;
  }
  .event-title sup { font-size: 26px; vertical-align: 20px; }
  .event-mark {
    position: absolute; left: 0; right: 0; top: 268px;
    text-align: center; color: var(--gold); font-weight: 600;
  }
  .event-mark .mark-dot {
    display: block; width: 30px; height: 30px; border-radius: 50%;
    background: var(--gold); margin: 0 auto 8px;
  }
  .event-mark .mark-name { font-size: 34px; line-height: 1.05; display: block; }
  .event-mark .mark-year { font-size: 34px; line-height: 1.05; display: block; }
  .club-name {
    position: absolute; left: 0; right: 0; top: 484px;
    text-align: center; color: var(--cream);
    font-weight: 600; font-size: 17px; line-height: 1.3;
  }
  .divider {
    position: absolute; left: 118px; top: 540px; width: 222px; height: 8px;
  }
  .doc-title {
    position: absolute; left: 0; right: 0; top: 556px;
    text-align: center; color: var(--gold);
    font-weight: 600; font-size: 34px; line-height: 1.25;
  }
</style>
</head>
<body>
  <main class="spread">
    <section class="back-page">
      <div class="address-plate">
        <p>Suite 2406<br>New York, NY.</p>
      </div>
    </section>

    <section class="front-page">
      <svg class="front-art" viewBox="0 0 458 651" width="458" height="651" aria-hidden="true">
        <defs>
          <linearGradient id="goldSweep" x1="0" x2="1" y1="0" y2="0">
            <stop offset="0" stop-color="#a9781f"/>
            <stop offset="0.35" stop-color="#f0d27a"/>
            <stop offset="0.7" stop-color="#c99a36"/>
            <stop offset="1" stop-color="#f0d27a"/>
          </linearGradient>
        </defs>
        <rect x="0" y="0" width="458" height="651" fill="#141414" role="img" aria-label="Subtle diamond lattice texture"/>
        <!-- upper sweep -->
        <path d="M0 138 Q229 262 458 160 L458 176 Q229 274 0 156 Z" fill="url(#goldSweep)"/>
        <!-- centre frame -->
        <path d="M21 203 Q229 279 437 203 L437 462 Q229 386 21 462 Z" fill="#161616" stroke="url(#goldSweep)" stroke-width="2"/>
        <!-- lower sweep -->
        <path d="M0 482 Q229 378 458 494 L458 510 Q229 392 0 500 Z" fill="url(#goldSweep)"/>
      </svg>

      <h1 class="event-title"><span>5<sup>th</sup>Annual</span><br>Lantern Dance</h1>

      <div class="event-mark">
        <span class="mark-dot"></span>
        <span class="mark-name">Lantern Dance</span>
        <span class="mark-year">2018</span>
      </div>

      <p class="club-name">University of Glenmarrow<br>Graduates Circle of New York</p>

      <svg class="divider" viewBox="0 0 222 8" aria-hidden="true">
        <line x1="0" y1="4" x2="104" y2="4" stroke="#d9ae4a" stroke-width="1.5"/>
        <rect x="107" y="0.5" width="6" height="6" transform="rotate(45 110 3.5)" fill="#d9ae4a"/>
        <line x1="118" y1="4" x2="222" y2="4" stroke="#d9ae4a" stroke-width="1.5"/>
      </svg>

      <h2 class="doc-title">Sponsorship<br>Brochure</h2>
    </section>
  </main>
</body>
</html>
```